Local Roofing/Construction company business needs new biz card design

We need a new business card design, current cards are from the start of this operation and generic at best. We are a local Construction Company (General Contractor) with a majority of our work originating from insurance claims-exterior finish work is the main focus (Roofs-Siding-Gutters etc). Heavily involved with homeowners and the low ball offers they receive from insurance company's after a insurable event takes place. I have attached some of our original logo file(s) below.

```html
<!DOCTYPE html>
<html lang="en">
<head>
<meta charset="utf-8">
<title>Stonecrest Builders – Business Card</title>
<link href="https://fonts.googleapis.com/css2?family=Open+Sans:wght@400;700&display=swap" rel="stylesheet">
<style>
  :root {
    --green: #55bd74;
    --ink: #1d1d1d;
    --dark: #142523;
    --rule: #444444;
    --card: #ffffff;
    --card-back: #f7f8f8;
    --backdrop: #e9e6e1;
  }
  * { box-sizing: border-box; margin: 0; padding: 0; }
  html, body { width: 1200px; height: 1200px; overflow: hidden; }
  body {
    background: var(--backdrop);
    font-family: "Open Sans", sans-serif;
    position: relative;
  }
  .card {
    position: absolute;
    left: 216px;
    width: 768px;
    height: 444px;
    border-radius: 26px;
    overflow: hidden;
    box-shadow: 0 18px 30px rgba(0,0,0,0.18);
  }
  .card--front { top: 70px; background: var(--card); }
  .card--back { top: 626px; background: var(--card-back); }

  .top-tab { position: absolute; left: 456px; top: 0; width: 266px; height: 38px; }

  .brand {
    position: absolute;
    display: flex;
    align-items: center;
    gap: 14px;
  }
  .brand__mark { width: 30px; height: 30px; background: var(--green); flex: none; }
  .brand__name { font-weight: 700; white-space: nowrap; }
  .card--front .brand { left: 40px; top: 80px; }
  .card--front .brand__name { font-size: 34px; color: var(--dark); }

  .identity {
    position: absolute;
    right: 40px;
    top: 254px;
    text-align: right;
  }
  .identity__name { font-size: 29px; font-weight: 700; color: var(--ink); line-height: 1.2; }
  .identity__role { font-size: 19px; color: var(--green); line-height: 1.35; }

  .divider {
    position: absolute;
    left: 40px;
    top: 299px;
    width: 480px;
    height: 1.5px;
    background: var(--rule);
  }

  .contacts {
    position: absolute;
    left: 38px;
    top: 314px;
    list-style: none;
  }
  .contacts li {
    display: flex;
    align-items: center;
    gap: 7px;
    font-size: 18px;
    color: var(--ink);
    line-height: 26px;
  }
  .contacts svg { width: 16px; height: 16px; flex: none; }

  .card--back .brand {
    left: 50%;
    top: 50%;
    transform: translate(-50%, -50%);
    gap: 16px;
  }
  .card--back .brand__mark { width: 40px; height: 40px; }
  .card--back .brand__name { font-size: 40px; color: var(--green); }
</style>
</head>
<body>
  <section class="card card--front" aria-label="Business card front">
    <svg class="top-tab" viewBox="0 0 266 38" aria-hidden="true">
      <path d="M0 0 H266 L242 30 Q236 38 224 38 H42 Q30 38 24 30 Z" fill="var(--green)"/>
    </svg>

    <div class="brand">
      <span class="brand__mark"></span>
      <span class="brand__name">Stonecrest Builders</span>
    </div>

    <div class="identity">
      <p class="identity__name">Marcus Delaney</p>
      <p class="identity__role">Chief Operating Officer</p>
    </div>

    <div class="divider"></div>

    <ul class="contacts">
      <li>
        <svg viewBox="0 0 16 16" fill="none" stroke="var(--green)" stroke-width="1.2"><path d="M8 15s5-5.2 5-8.6A5 5 0 0 0 3 6.4C3 9.8 8 15 8 15z"/><circle cx="8" cy="6.4" r="1.9"/></svg>
        482 Harbor Ave, Suite 2, Millbrook, NY 12545
      </li>
      <li>
        <svg viewBox="0 0 16 16" fill="none" stroke="var(--green)" stroke-width="1.2"><path d="M3.2 1.5l2.4.4 1 3-1.6 1.3a9 9 0 0 0 4.8 4.8l1.3-1.6 3 1 .4 2.4c-.8.9-2 1.5-3.3 1.3C6.8 13.4 2.6 9.2 1.9 4.8c-.2-1.3.4-2.5 1.3-3.3z"/></svg>
        +1 555-214-7730
      </li>
      <li>
        <svg viewBox="0 0 16 16" fill="none" stroke="var(--green)" stroke-width="1.2"><rect x="1.5" y="3.5" width="13" height="9.5" rx="1"/><path d="M1.8 4l6.2 5 6.2-5"/></svg>
        hello@stonecrestbuilders.com
      </li>
    </ul>
  </section>

  <section class="card card--back" aria-label="Business card back">
    <div class="brand">
      <span class="brand__mark"></span>
      <span class="brand__name">Stonecrest Builders</span>
    </div>
  </section>
</body>
</html>
```